Our architectural studio needs a new business card

We need a business card design for our studio based in Waterloo in Belgium. We are active in architecture, design and installation.
Our works are contemporary and minimalist. our clients are refined and cultured.
Our business card must be minimalist and refined.

Project Deadline Extended
Reason: Some designers have accepted my invitation but they don't have all replied. I want to give them a chance to make one proposal. Paul

Target Market(s)

architecture

Industry/Entity Type

Business

Contact Information for Business Card

studio: paul dornevaux studio
paul dornevaux, architecte
M. +32 471 586 927
F. +322 619 4850
www.pauldornevaux-example.com
paul@pauldornevaux-example.com
14 rue des Marronniers
1420 Waterloo
Belgium

Font styles to use
Sans Serif

Requirements
Must have
• simple, minimalist, clear, elegant and chic! Black and white
Nice to have
• embossed logo, other format like a square for example
Should not have
• color, fantasy, curves, ...

```html
<!DOCTYPE html>
<html lang="fr">
<head>
<meta charset="utf-8">
<title>Paul Dornevaux Studio – carte de visite</title>
<link rel="stylesheet" href="https://fonts.googleapis.com/css2?family=Nunito+Sans:wght@300;400&display=swap">
<style>
  :root {
    --slate: #404a4c;
    --ink: #111111;
    --paper: #ffffff;
    --frame: #000000;
  }
  * { box-sizing: border-box; margin: 0; padding: 0; }
  html, body {
    width: 1052px; height: 1200px; overflow: hidden;
    background: var(--paper);
    font-family: "Nunito Sans", sans-serif;
  }
  .canvas { position: relative; width: 1052px; height: 1200px; }

  .card {
    position: absolute; left: 0; width: 1052px;
    border: 2px solid var(--frame);
    overflow: hidden;
  }
  .card--front { top: 0; height: 586px; background: var(--slate); }
  .card--back  { top: 615px; height: 584px; background: var(--paper); }

  .card__white-panel { position: absolute; top: 0; left: 0; width: 254px; height: 100%; background: var(--paper); }
  .card__slate-panel { position: absolute; top: 0; left: 0; width: 254px; height: 100%; background: var(--slate); }

  /* front: studio name as mark */
  .front-mark {
    position: absolute; right: 40px; top: 120px;
    display: flex; align-items: center; gap: 22px;
    color: var(--paper); font-weight: 300;
    font-size: 64px; line-height: 1.05; text-align: right;
    letter-spacing: 2px;
  }
  .front-mark__square { width: 34px; height: 34px; background: var(--paper); flex: none; }

  .front-name {
    position: absolute; left: 72px; top: 482px;
    font-size: 40px; font-weight: 400; letter-spacing: 19.5px;
    color: var(--ink); white-space: nowrap;
  }

  /* back */
  .back-mark {
    position: absolute; left: 40px; top: 80px; width: 180px;
    color: var(--paper); font-weight: 300;
    font-size: 30px; line-height: 1.15; letter-spacing: 1px;
  }
  .back-title {
    position: absolute; left: 268px; top: 70px;
    font-size: 49px; font-weight: 400; letter-spacing: 2.5px;
    color: var(--slate); white-space: nowrap;
  }
  .back-role {
    position: absolute; left: 287px; top: 148px; width: 730px;
    display: flex; justify-content: space-between;
    font-size: 42px; font-weight: 400; color: var(--ink);
  }
  .back-contacts {
    position: absolute; left: 254px; right: 0; top: 230px;
    text-align: center; color: var(--ink);
    list-style: none;
  }
  .back-contacts li { font-size: 33px; letter-spacing: 3px; height: 70px; line-height: 70px; }
  .back-contacts li.tel { letter-spacing: 2.5px; height: 66px; line-height: 66px; }
  .back-address {
    position: absolute; left: 108px; top: 512px;
    font-size: 31.5px; letter-spacing: 2px; white-space: nowrap;
    background: linear-gradient(to right, var(--paper) 146px, var(--ink) 146px);
    -webkit-background-clip: text; background-clip: text;
    color: transparent;
  }
</style>
</head>
<body>
<main class="canvas">
  <section class="card card--front" aria-label="Recto">
    <div class="card__white-panel"></div>
    <div class="front-mark">
      <span class="front-mark__square"></span>
      <span>Paul<br>Dornevaux</span>
    </div>
    <p class="front-name">PAUL DORNEVAUX STUDIO</p>
  </section>

  <section class="card card--back" aria-label="Verso">
    <div class="card__slate-panel"></div>
    <p class="back-mark">Paul<br>Dornevaux</p>
    <h1 class="back-title">PAUL DORNEVAUX STUDIO</h1>
    <p class="back-role"><span>a</span><span>r</span><span>c</span><span>h</span><span>i</span><span>t</span><span>e</span><span>c</span><span>t</span><span>e</span></p>
    <ul class="back-contacts">
      <li>www.pauldornevaux-example.com</li>
      <li>paul@pauldornevaux-example.com</li>
      <li class="tel">M. +32 471 586 927</li>
      <li class="tel">F. +322 619 4850</li>
    </ul>
    <p class="back-address">rue des Marronniers 1420 Waterloo Belgium 14</p>
  </section>
</main>
</body>
</html>
```